Buch-/E-Book-Cover zum Thema Veltra Code
Zielgruppe
Hallo lieber Designer,
ich arbeite an einem Buch zum Thema Veltra Code. Dies ist ein System der Persönlichkeitsentwicklung.
Die Zielgruppe sind also Männer und Frauen mittleren Alters, die nach spiritueller Erfüllung und Selbsterkenntnis streben. Das Buchcover sollte dementsprechend esoterisch und meditativ angehaucht, aber trotzdem klar und modern strukturiert sein.
Du kannst dich gerne bei schon bestehenden Buchdesigns inspirieren lassen (Veltra Code Bücher auf Bücherkai)!
Die Zeichnung der sitzenden Menschen auf den Covern nennen sich Body Chart, falls du es für dein Design brauchst.
Ich habe aber extra nicht an den Reglern unten geschoben, damit du deine Kreativität ausleben kannst.
Aufgabenstellung
Der Auftrag beinhaltet die Buchvorderseite, die Rückseite UND den Buchrücken (die Spine). Deswegen habe ich das Preisgeld angehoben.
Vorder- und Rückseite haben ein Format von 6*9 Zoll, also 6 Zoll breit und 9 Zoll hoch. Der Buchrücken ist 0,338 Zoll breit und ebenfalls 9 Zoll hoch. Ich habe eine PNG-Datei angehängt, die das Ganze noch einmal visualisiert. Es wäre gut, wenn du dein Design dann auch in der gleichen Konstellation hochlädst (Rückseite, Rücken, Vorderseite). Außerdem braucht das Design an jeder Außenseite eine Beschnittzugabe von 0,125 Zoll. Deswegen ist die Gesamtdatei 12,533 * 9,25 Zoll groß. Auf dieser Beschnittzugabe kann das Design gerne noch weitergehen, damit keine unsauberen Bereiche beim Beschneiden entstehen. Es sollte aber kein Text mehr darauf vorhanden sein.
Vorderseite:
Titel: 'Veltra Code – Das Kleine Nordlicht 40 Schritte durch alte Muster im Veltra Code Modell für mehr Ruhe im Alltag und einen klaren Blick auf die eigene innere Mitte'
• Muss komplett und in Gänze vorne auf dem Buchcover drauf sein
• Highlight auf „Veltra Code – Das Kleine Nordlicht“
• Den Rest des Titels in kleinerer Schrift, aber trotzdem auf dem Cover
Autorenname: Jonas Kreuder
• Auch etwas größer als der Nebentitel
Buchrücken (Spine):
• nur „Veltra Code - Das Kleine Nordlicht“ (nicht den restlichen Titel) und den Namen des Autors
Rückseite:
Klappentext:
'Gehe auf die Reise zu Deinem wahren Ich
Beim Veltra-Code-Modell geht es um die Persönlichkeit und die individuelle Weiterentwicklung. Die Zielsetzung besteht darin, jedem Menschen zu ermöglichen, ein erfolgreiches, selbstbestimmtes und erfülltes Leben zu führen. Um dieses Ziel zu erreichen, ist es wichtig, die eigenen Stärken und Schwächen sowie die im Geburtshoroskop festgelegten Persönlichkeitsstrukturen zu kennen und zu berücksichtigen.
Dieses einzigar..

```html
<!DOCTYPE html>
<html lang="de">
<head>
<meta charset="utf-8">
<title>Veltra Code – Das Kleine Nordlicht · Umschlag</title>
<link rel="stylesheet" href="https://fonts.googleapis.com/css2?family=Archivo+Black&family=Archivo:wght@700&family=EB+Garamond:wght@400&display=swap">
<style>
  :root {
    --navy: #141b31;
    --gold: #e9a52c;
    --gold-light: #f6bd45;
    --gold-deep: #d18a1c;
    --title-gold: #e4ad48;
    --paper: #f2f1ee;
    --ink: #111111;
    --stage: #e4e4e4;
  }
  * { margin: 0; padding: 0; box-sizing: border-box; }
  html, body { width: 1200px; height: 1200px; overflow: hidden; background: var(--stage); }
  .canvas { position: relative; width: 1200px; height: 1200px; }

  .cover-wrap {
    position: absolute; left: 40px; top: 190px;
    width: 1120px; height: 821px;
    background: var(--navy);
    overflow: hidden;
  }

  .gold-texture {
    background:
      radial-gradient(ellipse at 30% 20%, var(--gold-light) 0%, transparent 55%),
      radial-gradient(ellipse at 75% 80%, var(--gold-deep) 0%, transparent 60%),
      linear-gradient(135deg, var(--gold) 0%, var(--gold-light) 45%, var(--gold-deep) 100%);
  }

  /* Rückseite */
  .back-panel {
    position: absolute; left: 0; top: 0;
    width: 575px; height: 410px;
  }
  .bleed-strip {
    position: absolute; left: 0; top: 186px;
    width: 39px; height: 482px;
    background: var(--paper);
  }
  .blurb {
    position: absolute; left: 50px; top: 36px; width: 480px;
    text-align: center; color: var(--ink);
  }
  .blurb-heading {
    font-family: "Archivo", Arial, sans-serif; font-weight: 700;
    font-size: 16.5px; margin-bottom: 52px;
  }
  .blurb-text {
    font-family: "EB Garamond", Georgia, serif;
    font-size: 14.6px; line-height: 19.4px;
  }
  .blurb-text + .blurb-text { margin-top: 19px; }

  /* Buchrücken */
  .spine-text {
    position: absolute; left: 557px;
    font-family: "EB Garamond", Georgia, serif; white-space: nowrap;
    transform-origin: 0 0;
  }
  .spine-author {
    top: 122px; color: var(--ink); font-size: 15px;
    transform: rotate(-90deg) translateY(-50%);
  }
  .spine-title {
    top: 760px; color: var(--title-gold); font-size: 15px;
    transform: rotate(-90deg) translateY(-50%);
  }

  /* Vorderseite */
  .front { position: absolute; left: 575px; top: 0; width: 545px; height: 821px; }
  .front-title {
    position: absolute; left: 0; width: 545px; top: 30px;
    text-align: center; color: var(--title-gold);
    font-family: "Archivo Black", "Arial Black", sans-serif; font-weight: 400;
  }
  .front-title .main { display: block; font-size: 58px; line-height: 68px; letter-spacing: 0.5px; }
  .front-title .sub { display: block; font-size: 37.5px; line-height: 46px; letter-spacing: 0.3px; }
  .subtitle {
    position: absolute; left: 22px; width: 501px; top: 162px;
    text-align: center; color: #ffffff;
    font-family: "EB Garamond", Georgia, serif;
    font-size: 18.5px; line-height: 23.5px;
  }
  .body-chart {
    position: absolute; left: 41px; top: 265px;
    width: 461px; height: 461px; border-radius: 50%;
    background: radial-gradient(circle at 50% 50%,
      var(--paper) 0%, var(--paper) 42%, var(--navy) 56%, var(--navy) 80%,
      var(--gold) 84%, var(--gold-deep) 92%, var(--navy) 96%);
  }
  .author-box {
    position: absolute; left: 175px; top: 760px;
    width: 196px; height: 61px;
    display: flex; align-items: center; justify-content: center;
    font-family: "EB Garamond", Georgia, serif; font-size: 17.5px; color: var(--ink);
  }
</style>
</head>
<body>
<main class="canvas">
  <section class="cover-wrap">
    <div class="back-panel gold-texture"></div>
    <div class="bleed-strip"></div>
    <div class="blurb">
      <h2 class="blurb-heading">Gehe auf die Reise zu Deinem wahren Ich</h2>
      <p class="blurb-text">Beim Veltra-Code-Modell geht es um die Persönlichkeit und die individuelle Weiterentwicklung. Die Zielsetzung besteht darin, jedem Menschen zu ermöglichen, ein erfolgreiches, selbstbestimmtes und erfülltes Leben zu führen. Um dieses Ziel zu erreichen, ist es wichtig, die eigenen Stärken und Schwächen sowie die im Geburtshoroskop festgelegten Persönlichkeitsstrukturen zu kennen und zu berücksichtigen.</p>
      <p class="blurb-text">Dieses einzigartige System verbindet bewährte Traditionen und moderne Wissenschaften miteinander. Anhand Ihrer seelischen Landkarte werden individuelle Charaktereigenschaften und deren Auswirkungen auf den Lauf Ihres Lebens aufgezeigt. Es hilft dabei, Selbstakzeptanz und Selbstliebe zu entwickeln.</p>
    </div>

    <span class="spine-text spine-author">Jonas Kreuder</span>
    <span class="spine-text spine-title">Veltra Code - Das Kleine Nordlicht</span>

    <div class="front">
      <h1 class="front-title">
        <span class="main">Veltra Code</span>
        <span class="sub">Das Kleine Nordlicht</span>
      </h1>
      <p class="subtitle">40 Schritte durch alte Muster im Veltra Code Modell für mehr Ruhe im Alltag und einen klaren Blick auf die eigene innere Mitte</p>
      <div class="body-chart" role="img" aria-label="Illustration: Silhouette einer Frau mit goldenem Body Chart, umgeben von einem goldenen Pinselkreis"></div>
      <div class="author-box gold-texture">Jonas Kreuder</div>
    </div>
  </section>
</main>
</body>
</html>
```